Business Card Design

We are an IT staffing and consulting company providing IT solutions and resources to our clients.

Industry/Entity Type

Business

Contact Information for Business Card

Ravindra Kolluparthi
Vice President

BrimTrail Inc
48260 Hollyfern Market Court, suite 700
Ashburn, VA 20147
Direct: 571-555-0193
Mobile: 571-555-0147
Email: Ravindra@brimtrailinc.example
Fax: 703-555-0162
www.brimtrailinc.example

```html
<!DOCTYPE html>
<html lang="en">
<head>
<meta charset="utf-8">
<title>BrimTrail Inc – Business Card</title>
<link rel="stylesheet" href="https://fonts.googleapis.com/css2?family=Open+Sans:wght@400;600;700&display=swap">
<style>
  :root {
    --backdrop: #e4e4e4;
    --card-dark: #231f1e;
    --card-dark-edge: #2e2928;
    --card-light: #ffffff;
    --brand-red: #c41f24;
    --ink: #333333;
    --ink-soft: #555555;
    --logo-light: #d9d9d9;
    --band-dark: #1a1a1a;
  }
  * { box-sizing: border-box; margin: 0; padding: 0; }
  html, body {
    width: 1200px; height: 852px; overflow: hidden;
    background: var(--backdrop);
    font-family: "Open Sans", Arial, sans-serif;
  }
  .stage {
    position: relative; width: 1200px; height: 852px;
    display: flex; align-items: center; justify-content: center; gap: 50px;
  }
  .card {
    position: relative; width: 520px; height: 300px;
    border-radius: 22px; overflow: hidden;
    box-shadow: 0 6px 18px rgba(0,0,0,.18);
  }
  .card--front {
    background: radial-gradient(ellipse at 55% 40%, var(--card-dark-edge), var(--card-dark) 70%);
    display: flex; align-items: center; justify-content: center;
  }
  .brand-name {
    font-weight: 400; font-size: 44px; letter-spacing: 1px;
    line-height: 1;
  }
  .card--front .brand-name { color: var(--logo-light); }

  .card--back { background: var(--card-light); }
  .card--back .brand-name {
    position: absolute; right: 34px; top: 118px;
    font-size: 36px; color: var(--ink);
  }
  .holder { position: absolute; left: 30px; top: 34px; }
  .holder__name { color: var(--brand-red); font-weight: 700; font-size: 17px; }
  .holder__title { color: var(--ink-soft); font-size: 13px; margin-top: 1px; }
  .address {
    position: absolute; left: 30px; top: 112px;
    font-size: 12px; line-height: 1.4; color: var(--ink);
  }
  .contacts {
    position: absolute; left: 30px; top: 160px;
    list-style: none; font-size: 12px; color: var(--ink);
  }
  .contacts li { display: flex; align-items: center; gap: 10px; height: 18px; }
  .contacts svg { width: 11px; height: 11px; fill: var(--brand-red); flex: none; }
  .contacts .accent { color: var(--brand-red); }
  .band { position: absolute; left: 0; bottom: 0; width: 520px; height: 60px; }
</style>
</head>
<body>
<main class="stage">
  <section class="card card--front" aria-label="Card front">
    <span class="brand-name">BrimTrail</span>
  </section>

  <section class="card card--back" aria-label="Card back">
    <div class="holder">
      <p class="holder__name">Ravindra Kolluparthi</p>
      <p class="holder__title">Vice President</p>
    </div>

    <span class="brand-name">BrimTrail</span>

    <p class="address">48260 Hollyfern Market Court,<br>suite 700 Ashburn, VA 20147</p>

    <ul class="contacts">
      <li><svg viewBox="0 0 12 12"><path d="M2 1h3l1 3-2 1c.6 1.4 1.6 2.4 3 3l1-2 3 1v3c-5.5 0-9-3.5-9-9z"/></svg>571-555-0193</li>
      <li><svg viewBox="0 0 12 12"><path d="M3 0h6v12H3zM4 1.5v8h4v-8z"/></svg>571-555-0147</li>
      <li><svg viewBox="0 0 12 12"><path d="M3 0h6v3H3zM1 4h10v5H9v3H3V9H1zm3 4v3h4V8z"/></svg>703-555-0162</li>
      <li><svg viewBox="0 0 12 12"><path d="M0 2h12v8H0zm1 1v.5l5 3.5 5-3.5V3z"/></svg>Ravindra@brimtrailinc.example</li>
      <li><svg viewBox="0 0 12 12"><circle cx="6" cy="6" r="5.5"/></svg>www.<span class="accent">brimtrailinc</span>.example</li>
    </ul>

    <svg class="band" viewBox="0 0 520 60" preserveAspectRatio="none" aria-hidden="true">
      <path d="M0 48 L300 48 L330 18 L520 18 L520 60 L0 60 Z" fill="var(--brand-red)"/>
      <path d="M440 18 L520 18 L520 60 L480 60 Z" fill="var(--band-dark)"/>
    </svg>
  </section>
</main>
</body>
</html>
```